Header-Banner für Newsletter-/Journey-Mails
Zielgruppe
Wir, der Morvik Verlag sind der führende Verlag für Kinderbücher und Comics.
Aufgabenstellung
Wir suchen übergangsweise - bis zum Relaunch unserer Website - einen Header-Banner für unserer Newsletter/Journey-Mails.
Das Morvik Comics Logo sollte enthalten sein. Das Design des Banner sollte eine moderne, nicht verspielte, anspruchsvolle, grafisch orientierte Zielgruppe ansprechen.
Bitte keine Fotos und nicht selbst illustrieren.
Maße: Breite 600 px - Höhe max. 300 Pixel.

```html
<!DOCTYPE html>
<html lang="de">
<head>
<meta charset="utf-8">
<title>Newsmail Nr. 12 | 2019 – Morvik Comics</title>
<link rel="stylesheet" href="https://fonts.googleapis.com/css2?family=Sniglet:wght@400;800&display=swap">
<style>
  :root {
    --sky: #3dbfe0;
    --sky-deep: #2bb2d8;
    --sun: #ffd41f;
    --ink: #1f1f1f;
    --paper: #ffffff;
    --shade: #3a3a3a;
    --issue: #2aaed4;
    --brand: #f39a1e;
  }
  * { margin: 0; padding: 0; box-sizing: border-box; }
  html, body {
    width: 1200px;
    height: 500px;
    overflow: hidden;
    background: var(--paper);
  }
  .banner {
    position: relative;
    width: 1200px;
    height: 500px;
    overflow: hidden;
    font-family: "Sniglet", "Arial Rounded MT Bold", sans-serif;
  }
  .banner__backdrop {
    position: absolute;
    inset: 0;
    background: linear-gradient(135deg, var(--sky) 0%, #58c6d0 55%, var(--sky-deep) 100%);
  }
  .banner__bubble {
    position: absolute;
    inset: 0;
    width: 1200px;
    height: 500px;
  }
  .bubble__shadow { fill: var(--shade); }
  .bubble__body {
    fill: var(--paper);
    stroke: var(--ink);
    stroke-width: 9;
    stroke-linejoin: round;
  }
  .banner__title {
    position: absolute;
    left: 0;
    top: 78px;
    width: 1080px;
    text-align: center;
    font-weight: 800;
    font-size: 158px;
    line-height: 1;
    letter-spacing: 2px;
    color: var(--sun);
    -webkit-text-stroke: 12px var(--ink);
    paint-order: stroke fill;
  }
  .banner__issue {
    position: absolute;
    left: 548px;
    top: 214px;
    font-weight: 800;
    font-size: 38px;
    line-height: 1;
    letter-spacing: 1px;
    color: var(--issue);
  }
  .brand {
    position: absolute;
    right: 26px;
    bottom: 30px;
    display: flex;
    align-items: center;
    gap: 10px;
  }
  .brand__mark {
    width: 26px;
    height: 26px;
    background: var(--brand);
  }
  .brand__name {
    font-weight: 800;
    font-size: 30px;
    line-height: 1;
    color: var(--brand);
  }
</style>
</head>
<body>
  <header class="banner">
    <div class="banner__backdrop" role="img" aria-label="Hellblauer Hintergrund mit gelbem Punktraster im Comic-Stil"></div>

    <svg class="banner__bubble" viewBox="0 0 1200 500" aria-hidden="true">
      <path class="bubble__shadow" d="M -20,-20 L 995,-20 Q 1010,180 985,368 Q 980,395 950,395 L 660,400 L 610,486 L 570,406 L 40,418 Q -10,420 -10,388 Z"/>
      <path class="bubble__body" d="M -20,-20 L 985,-20 Q 1000,180 975,358 Q 970,385 940,385 L 650,390 L 600,476 L 560,396 L 30,408 Q -20,410 -20,378 Z"/>
    </svg>

    <h1 class="banner__title">Newsmail</h1>
    <p class="banner__issue">Nr. 12 | 2019</p>

    <div class="brand" aria-label="Morvik Comics">
      <span class="brand__mark"></span>
      <span class="brand__name">Morvik Comics</span>
    </div>
  </header>
</body>
</html>
```